Coastal Sentinels Stationery Design Project

I am looking for a suitable stationary design for my company Coastal Sentinels Pty Ltd (ACN 508 214 396).

The requirements can be better explained by visiting my website
"coastal-sentinels.org"

I will be sending letters to Ministers of State and the Heads of Government Agencies so the theme needs to be formal and serious.

A theme with a shield or similar picking on the "guardian" concept would be appropriate

Target Market(s)

Ministers of State and Department Agency Heads and legal firms, the heads of Trustee Companies as well as Members of Coastal Sentinels

Industry/Entity Type

Government

Requirements
Must have
• Letterhead design is a priority - Business Card secondary

Must include tag line "Shielding your savings when the rest walk away" with a registered trade mark superscript at the end that is an R in a circle {Windows Alt +0174 on numeric keypad or Mac Option +R}.

Must include website address "Coastal-Sentinels.org" plus Email address "coastsentinel@fernmail.net

Company name "Coastal Sentinels Pty. Ltd." and Australian Company Number "ACN 508 214 396" needs to be shown more discretely

Address is "47 Brookfern Lane, Marlow Vale, 3281"
Nice to have
• A watermark is something to be considered

```html
<!DOCTYPE html>
<html lang="en">
<head>
<meta charset="utf-8">
<title>Coastal Sentinels Stationery</title>
<link href="https://fonts.googleapis.com/css2?family=Arimo:wght@400;700&display=swap" rel="stylesheet">
<style>
  :root {
    --maroon: #6b0f3f;
    --maroon-dark: #4e0a2d;
    --ink: #1d1d1d;
    --paper: #ffffff;
    --mark: #ececec;
    --backdrop: #3c3c3c;
  }
  * { box-sizing: border-box; margin: 0; padding: 0; }
  html, body { width: 1200px; height: 960px; overflow: hidden; }
  body {
    background: var(--backdrop);
    font-family: "Arimo", Arial, sans-serif;
    color: var(--ink);
    position: relative;
  }
  .sheet, .card { position: absolute; background: var(--paper); overflow: hidden; box-shadow: 0 8px 24px rgba(0,0,0,.45); }

  /* Shared brand block */
  .brand { position: absolute; display: flex; align-items: center; gap: 8px; }
  .brand-square { background: var(--maroon); flex: none; }
  .brand-name { font-weight: 700; color: var(--maroon); line-height: 0.95; white-space: nowrap; }
  .brand-tagline { color: var(--ink); margin-top: 3px; white-space: nowrap; }
  .brand-tagline sup { font-size: 0.8em; line-height: 0; }

  /* Letterhead */
  .letterhead { left: 50px; top: 40px; width: 620px; height: 877px; }
  .letterhead .brand { left: 52px; top: 62px; }
  .letterhead .brand-square { width: 22px; height: 22px; }
  .letterhead .brand-name { font-size: 17px; }
  .letterhead .brand-tagline { font-size: 7px; }

  .watermark { position: absolute; border-radius: 50%; background: var(--mark); }
  .letterhead .watermark { right: -40px; bottom: 40px; width: 240px; height: 240px; }

  .footer-info { position: absolute; left: 90px; top: 782px; font-size: 9.5px; line-height: 1.4; display: flex; gap: 50px; }
  .company { color: var(--maroon); font-weight: 700; }
  .label { color: var(--maroon); }
  .band { position: absolute; left: 0; bottom: 0; width: 100%; }

  /* Business card front */
  .card { width: 460px; height: 262px; }
  .card-front { left: 700px; top: 150px; background: linear-gradient(100deg, #7a1349 0%, var(--maroon) 45%, var(--maroon-dark) 100%); }
  .card-front .brand { left: 58px; top: 92px; gap: 12px; }
  .card-front .brand-square { background: #fff; width: 40px; height: 40px; }
  .card-front .brand-name { color: #fff; font-size: 24px; }
  .card-front .brand-tagline { color: #fff; font-size: 9.5px; margin-top: 4px; }
  .card-front .web { position: absolute; right: 120px; bottom: 8px; color: var(--maroon); font-weight: 700; font-size: 10px; }

  /* Business card back */
  .card-back { left: 700px; top: 460px; }
  .card-back .brand { left: 26px; top: 24px; }
  .card-back .brand-square { width: 20px; height: 20px; }
  .card-back .brand-name { font-size: 15px; }
  .card-back .brand-tagline { font-size: 6.5px; }
  .card-back .watermark { right: -30px; top: 20px; width: 180px; height: 180px; }
  .holder { position: absolute; left: 34px; top: 92px; font-size: 10px; line-height: 1.35; }
  .holder-name { color: var(--maroon); font-weight: 700; font-size: 13px; }
  .holder .gap { height: 12px; }
</style>
</head>
<body>

<section class="sheet letterhead">
  <div class="brand">
    <span class="brand-square"></span>
    <div>
      <div class="brand-name">Coastal<br>Sentinels Pty Ltd</div>
      <div class="brand-tagline">Shielding Your Savings When The Rest Walk Away<sup>®</sup></div>
    </div>
  </div>
  <div class="watermark" role="img" aria-label="Faint watermark disc"></div>
  <div class="footer-info">
    <div>
      <div class="company">Coastal Sentinels Pty Ltd</div>
      <div>47 Brookfern Lane, Marlow Vale, 3281</div>
      <div>ACN 508 214 396</div>
    </div>
    <div>
      <div><span class="label">p:</span> 987.654.3210</div>
      <div><span class="label">e:</span> coastsentinel@fernmail.net</div>
      <div><span class="label">w:</span> www.Coastal-Sentinels.org</div>
    </div>
  </div>
  <svg class="band" width="620" height="60" viewBox="0 0 620 60" preserveAspectRatio="none">
    <path d="M0,42 C200,30 420,14 620,0 L620,60 L0,60 Z" fill="var(--maroon)"/>
  </svg>
</section>

<section class="card card-front">
  <div class="brand">
    <span class="brand-square"></span>
    <div>
      <div class="brand-name">Coastal<br>Sentinels Pty Ltd</div>
      <div class="brand-tagline">Shielding Your Savings When The Rest Walk Away<sup>®</sup></div>
    </div>
  </div>
  <svg class="band" width="460" height="40" viewBox="0 0 460 40" preserveAspectRatio="none">
    <path d="M0,28 C150,24 320,10 460,0 L460,40 L0,40 Z" fill="#fff"/>
  </svg>
  <div class="web">www.Coastal-Sentinels.org</div>
</section>

<section class="card card-back">
  <div class="watermark" role="img" aria-label="Faint watermark disc"></div>
  <div class="brand">
    <span class="brand-square"></span>
    <div>
      <div class="brand-name">Coastal<br>Sentinels Pty Ltd</div>
      <div class="brand-tagline">Shielding Your Savings When The Rest Walk Away<sup>®</sup></div>
    </div>
  </div>
  <div class="holder">
    <div class="holder-name">JOHN DOE</div>
    <div>Position</div>
    <div class="gap"></div>
    <div class="company">Coastal Sentinels Pty Ltd</div>
    <div>47 Brookfern Lane, Marlow Vale, 3281</div>
    <div class="gap"></div>
    <div><span class="label">p:</span> 987.654.3210</div>
    <div><span class="label">e:</span> coastsentinel@fernmail.net</div>
    <div><span class="label">w:</span> www.Coastal-Sentinels.org</div>
  </div>
  <svg class="band" width="460" height="34" viewBox="0 0 460 34" preserveAspectRatio="none">
    <path d="M0,26 C160,22 330,10 460,0 L460,34 L0,34 Z" fill="var(--maroon)"/>
  </svg>
</section>

</body>
</html>
```